Data Analytics Platform Website Design

Website design for a new data analytics platform called Metrica Core. I need a design that is simple but informative, professional but still sexy and that is aimed at the business professional instead of being "technical". I have a logo (picture uploaded) and also screenshots from the platform itself and I can also provide example websites from competitors that are similar in design and layout to what I need. I also have the messaging but I need help with photos, icons, font, layout, etc. I want to utilize some of the colors in the logo, but I want the overall color scheme to utilize darker blues (more serious feeling, less playful) with one accent color for highlighting. This design cannot be "fun", "playful", or "cheerful" and should instead be "professional", "serious", but still uncluttered and clean cut. However, simple does not mean easy because I want to see transitions that are clean and high level. I want the final design to be all of that while showing the company and our product as capable, serious, and reliable.

Example websites:
1. www.valdrenix.com
2. q7.ai
3. corvelane.com
4. https://www.pym.com/en_us/software/lorsa.html
5. https://www.belvoro.com/
6. gwendel.ai

Target Market(s)

Business Professionals - Government/large companies/data analytics focused

Industry/Entity Type

Data Science

Number of Pages Required

3 page

Font styles to use
Serif
Sans Serif

Requirements
Must have
• It must be clean and professional. Cannot be cluttered or too "busy". No playful or childish looks at all.
Nice to have
• I want to see professional designs but also professional concepts incorporated.
Should not have
• Should not have Comic Sans or the like, no playful or "techy" themes

```html
<!DOCTYPE html>
<html lang="en">
<head>
<meta charset="utf-8">
<title>Metrica Core — Data Analytics Platform</title>
<link rel="stylesheet" href="https://fonts.googleapis.com/css2?family=Montserrat:wght@400;500;600;700&family=Open+Sans:wght@400;600;700&display=swap">
<style>
:root{
  --navy:#081a47;
  --navy-deep:#050f2e;
  --ink:#0d0f1a;
  --blue:#2a7de1;
  --blue-bright:#3a8ef0;
  --pale:#f2f6fc;
  --white:#ffffff;
  --text:#2b2f3a;
  --muted:#8a90a0;
  --footer:#0e1128;
}
*{margin:0;padding:0;box-sizing:border-box}
html,body{width:1200px;height:3639px;overflow:hidden;background:var(--white)}
body{font-family:"Montserrat",sans-serif;color:var(--ink);position:relative}
.page{position:absolute;left:117px;top:109px;width:966px;height:3424px;overflow:hidden;background:var(--white)}
.abs{position:absolute}
.accent{color:var(--blue)}
.btn{position:absolute;display:flex;align-items:center;justify-content:center;background:var(--blue);color:var(--white);font-size:10px;font-weight:600;border-radius:3px;box-shadow:0 4px 10px rgba(42,125,225,.3)}
.h2{font-size:31px;font-weight:700;line-height:33px;letter-spacing:-.2px}
.copy{font-size:10.5px;line-height:17px;color:var(--text)}

/* hero */
.hero{left:0;top:0;width:966px;height:498px;background:linear-gradient(90deg,var(--navy-deep) 0%,var(--navy) 40%,#0a2358 100%)}
.hero-visual{left:330px;top:0;width:636px;height:498px;background:radial-gradient(ellipse at 65% 45%,rgba(40,120,190,.55) 0%,rgba(20,70,140,.35) 35%,rgba(8,26,71,0) 70%)}
.logo{display:flex;align-items:center;gap:8px;font-size:16px;font-weight:500;color:var(--white);letter-spacing:.3px}
.logo-mark{width:20px;height:20px;background:var(--blue-bright);border-radius:2px}
.nav{left:338px;top:28px;font-size:10.5px;font-weight:600;color:var(--white)}
.nav a{color:inherit;text-decoration:none;position:absolute;white-space:nowrap}
.nav .active{color:var(--blue-bright)}
.contact-btn{left:745px;top:18px;width:107px;height:34px;border:1px solid rgba(255,255,255,.8);border-radius:4px;color:var(--white);font-size:10.5px;font-weight:500;display:flex;align-items:center;justify-content:center}
.hero-title{left:110px;top:192px;font-size:30px;line-height:33px;font-weight:700;color:var(--white)}
.hero-title .accent{color:var(--blue-bright)}
.hero-copy{left:110px;top:268px;width:340px;font-size:10.5px;line-height:16px;color:#d6deef}

.band-pale{background:var(--pale)}

/* services */
.svc-card{left:479px;width:392px;height:104px;background:var(--white);border-radius:3px;box-shadow:0 6px 18px rgba(20,40,90,.08)}
.svc-icon{position:absolute;left:33px;top:26px;width:49px;height:49px;background:#eaf1fc;border-radius:4px;display:flex;align-items:center;justify-content:center}
.svc-title{position:absolute;left:97px;top:26px;font-size:12.5px;font-weight:600}
.svc-copy{position:absolute;left:97px;top:50px;width:260px;font-size:9px;line-height:15px;color:var(--muted)}

/* about visual */
.about-visual{left:470px;top:50px;width:320px;height:390px;border-radius:50%;background:radial-gradient(ellipse at 55% 50%,rgba(122,100,236,.75) 0%,rgba(110,110,240,.45) 35%,rgba(190,120,235,.15) 60%,rgba(255,255,255,0) 72%)}

/* blog */
.blog-title{left:0;width:966px;top:2614px;text-align:center;font-size:30px;font-weight:600}
.card{top:2690px;width:256px;height:294px;background:var(--white);box-shadow:0 4px 14px rgba(20,40,90,.05)}
.card-img{position:absolute;left:20px;top:15px;width:216px;height:103px}
.card-meta{position:absolute;left:20px;top:130px;font-size:8px;color:var(--muted);font-family:"Open Sans",sans-serif}
.card-head{position:absolute;left:20px;top:150px;width:216px;font-family:"Open Sans",sans-serif;font-size:14.5px;line-height:23px;font-weight:700;color:var(--ink)}
.card-copy{position:absolute;left:20px;top:205px;width:216px;font-family:"Open Sans",sans-serif;font-size:10px;line-height:17px;color:var(--text)}
.card-link{position:absolute;left:20px;top:262px;font-family:"Open Sans",sans-serif;font-size:11.5px;font-weight:700;color:var(--blue)}
.arrows{left:32px;top:3025px;width:82px;height:36px;background:var(--white);display:flex;align-items:center;justify-content:space-around;box-shadow:0 2px 8px rgba(20,40,90,.06)}

/* footer */
.footer{left:0;top:3126px;width:966px;height:298px;background:var(--footer);color:var(--white)}
.foot-copy{font-size:10px;line-height:17px;color:#d0d4e2}
.foot-head{font-size:10.5px;font-weight:600}
.foot-link{font-size:9px;color:#d0d4e2;position:absolute;white-space:nowrap}
.social{width:26px;height:26px;background:var(--white);border-radius:2px}
</style>
</head>
<body>
<div class="page">

  <section class="abs hero">
    <div class="abs hero-visual" role="img" aria-label="Glowing network of connected data points forming a human head profile"></div>
    <div class="abs logo" style="left:110px;top:26px"><span class="logo-mark"></span>Metrica Core</div>
    <nav class="abs nav">
      <a class="active" style="left:0;top:0">Home</a>
      <a style="left:70px;top:0">Who We Are</a>
      <a style="left:175px;top:0">Service</a>
      <a style="left:251px;top:0">Platform</a>
      <a style="left:334px;top:0">Blog</a>
    </nav>
    <div class="abs contact-btn">Contact Us</div>
    <h1 class="abs hero-title">Based on the data<br><span class="accent">make wise</span> decisions</h1>
    <p class="abs hero-copy">Lorem ipsum dolor sit amet, consectetur adipiscing elit. Non elit, a in orci. Nisl volutpat, eros mauris diam elementum .</p>
    <div class="btn" style="left:110px;top:323px;width:99px;height:27px">Learn More</div>
  </section>

  <section class="abs band-pale" style="left:0;top:498px;width:966px;height:485px">
    <div class="abs" style="left:0;top:77px;width:483px;height:335px;background:linear-gradient(135deg,#0b1a33 0%,#1a3150 55%,#0c1a2c 100%)" role="img" aria-label="Analyst working late at a desk surrounded by streams of data"></div>
    <h2 class="abs h2" style="left:522px;top:126px">Scale. <span class="accent">Interactivity.</span><br>Choose One Two.</h2>
    <p class="abs copy" style="left:522px;top:205px;width:335px">Interactively query, visualize, and power data science workflows over billions of records, no downsampling or pre-aggregation required. Valdrenix leverages the full power and parallelism of modern hardware, both CPU and GPU, to allow you to explore and extract insight from your largest datasets without lag.</p>
    <div class="btn" style="left:522px;top:320px;width:101px;height:29px">Learn More</div>
  </section>

  <section class="abs" style="left:0;top:983px;width:966px;height:459px">
    <h2 class="abs h2" style="left:118px;top:105px">Where <span class="accent">Data<br>Science</span> and<br>Analytics Converge</h2>
    <p class="abs copy" style="left:118px;top:219px;width:335px">Break down silos with the only open platform that unites analytics, data science and location intelligence workflows. Leverage native SQL, interactive visual analytics, extensive Pylon stack integrations, and a powerful machine learning framework.</p>
    <div class="btn" style="left:118px;top:330px;width:101px;height:28px">Learn More</div>
    <div class="abs" style="left:510px;top:60px;width:456px;height:335px;background:linear-gradient(120deg,#1b2d44 0%,#2a4a68 45%,#0f2238 100%)" role="img" aria-label="Data scientist reviewing charts projected in front of her"></div>
  </section>

  <section class="abs band-pale" style="left:0;top:1442px;width:966px;height:593px">
    <div class="abs" style="left:0;top:0;width:441px;height:593px;background:radial-gradient(ellipse at 45% 55%,#e9793a 0%,#8a4a3a 30%,#2d3550 65%,#1a2238 100%)" role="img" aria-label="Hands holding a tablet with glowing holographic charts"></div>
    <h2 class="abs h2" style="left:479px;top:60px">Our <span class="accent">Services</span></h2>
    <p class="abs copy" style="left:479px;top:107px;width:400px">Lorem ipsum dolor sit amet, consectetur adipiscing elit. Pellentesque diam dolor, id lorem integer mauris, at porttitor elit.</p>

    <div class="abs svc-card" style="top:190px">
      <div class="svc-icon"><svg width="18" height="20" viewBox="0 0 18 20"><ellipse cx="9" cy="4" rx="8" ry="3.2" fill="#2a7de1"/><path d="M1 7.5c0 1.8 3.6 3.2 8 3.2s8-1.4 8-3.2v3.5c0 1.8-3.6 3.2-8 3.2S1 12.8 1 11z" fill="#2a7de1"/><path d="M1 14c0 1.8 3.6 3.2 8 3.2s8-1.4 8-3.2v2.3c0 1.8-3.6 3.2-8 3.2s-8-1.4-8-3.2z" fill="#2a7de1"/></svg></div>
      <div class="svc-title">Intelligent observability</div>
      <div class="svc-copy">Lorem ipsum dolor sit amet, consectetur adipiscing elit. Scelerisque ipsum ipsum.</div>
    </div>
    <div class="abs svc-card" style="top:313px">
      <div class="svc-icon"><svg width="18" height="20" viewBox="0 0 18 20"><rect x="1" y="1" width="13" height="17" rx="1.5" fill="none" stroke="#2a7de1" stroke-width="2"/><line x1="4" y1="6" x2="11" y2="6" stroke="#2a7de1" stroke-width="1.8"/><circle cx="11" cy="13" r="3" fill="none" stroke="#2a7de1" stroke-width="1.8"/><line x1="13" y1="15" x2="16.5" y2="18.5" stroke="#2a7de1" stroke-width="2"/></svg></div>
      <div class="svc-title">Continous Automation</div>
      <div class="svc-copy">Lorem ipsum dolor sit amet, consectetur adipiscing elit. Scelerisque ipsum ipsum.</div>
    </div>
    <div class="abs svc-card" style="top:436px">
      <div class="svc-icon"><svg width="18" height="18" viewBox="0 0 18 18"><rect x="1" y="10" width="4" height="7" fill="#2a7de1"/><rect x="7" y="6" width="4" height="11" fill="#2a7de1"/><rect x="13" y="1" width="4" height="16" fill="#2a7de1"/></svg></div>
      <div class="svc-title">Ai- Assistance</div>
      <div class="svc-copy">Lorem ipsum dolor sit amet, consectetur adipiscing elit. Scelerisque ipsum ipsum.</div>
    </div>
  </section>

  <section class="abs" style="left:0;top:2035px;width:966px;height:518px">
    <h2 class="abs h2" style="left:118px;top:152px">About <span class="accent">Metrica<br>Core</span></h2>
    <p class="abs copy" style="left:118px;top:233px;width:335px">Break down silos with the only open platform that unites analytics, data science and location intelligence workflows. Leverage native SQL, interactive visual analytics, extensive Pylon stack integrations, and a powerful machine learning framework.</p>
    <div class="btn" style="left:118px;top:343px;width:101px;height:28px">Learn More</div>
    <div class="abs about-visual" role="img" aria-label="Isometric rising bar chart in purple and blue"></div>
  </section>

  <section class="abs band-pale" style="left:0;top:2553px;width:966px;height:573px"></section>
  <h2 class="abs blog-title">Latest Blog <span class="accent">Articles</span></h2>

  <article class="abs card" style="left:73px">
    <div class="card-img" style="background:linear-gradient(180deg,#8fbfe0 0%,#9bb3c4 55%,#a48f7a 100%)" role="img" aria-label="Industrial power facility under a blue sky"></div>
    <div class="card-meta">By Admin, on Nov 23th, 2020 &nbsp;|&nbsp; 1 days ago</div>
    <h3 class="card-head">Vorelio secures order for Canadian power provider</h3>
    <p class="card-copy">Vorelio secures order for Canadian power provider through reseller Brantel Highlights: Canadian power</p>
    <div class="card-link">Read more</div>
  </article>
  <article class="abs card" style="left:354px">
    <div class="card-img" style="background:linear-gradient(180deg,#c9b9a4 0%,#3a3f45 45%,#2b3a44 70%,#c4ab8c 100%)" role="img" aria-label="Laptop on a desk showing market charts"></div>
    <div class="card-meta">By Admin, on Nov 23th, 2020 &nbsp;|&nbsp; 1 days ago</div>
    <h3 class="card-head">A real opportunity for investors in Vorelio</h3>
    <p class="card-copy">Owen Marsden, CEO and Investment Advisor at Harlow Capital Partners chats with Teodora</p>
    <div class="card-link">Read more</div>
  </article>
  <article class="abs card" style="left:635px">
    <div class="card-img" style="background:linear-gradient(180deg,#8fbfe0 0%,#9bb3c4 55%,#a48f7a 100%)" role="img" aria-label="Industrial power facility under a blue sky"></div>
    <div class="card-meta">By Admin, on Nov 23th, 2020 &nbsp;|&nbsp; 1 days ago</div>
    <h3 class="card-head">Vorelio’s receives four new orders from US state</h3>
    <p class="card-copy">Vorelio receives four new orders for its video analytics and motion intelligence platform from reseller</p>
    <div class="card-link">Read more</div>
  </article>

  <div class="abs arrows">
    <svg width="20" height="10" viewBox="0 0 20 10"><path d="M19 5H2M6 1L2 5l4 4" fill="none" stroke="#2a7de1" stroke-width="1.6"/></svg>
    <svg width="20" height="10" viewBox="0 0 20 10"><path d="M1 5h17M14 1l4 4-4 4" fill="none" stroke="#2a7de1" stroke-width="1.6"/></svg>
  </div>
  <div class="btn" style="left:753px;top:3023px;width:107px;height:31px;font-size:10.5px">See More</div>

  <footer class="abs footer">
    <div class="abs logo" style="left:108px;top:64px"><span class="logo-mark"></span>Metrica Core</div>
    <p class="abs foot-copy" style="left:110px;top:100px;width:230px">Interactively query, visualize, and power data science workflows over billions of records, no downsampling</p>
    <div class="abs foot-head" style="left:431px;top:67px">Menu</div>
    <span class="foot-link" style="left:431px;top:104px">Haqqımızda</span>
    <span class="foot-link" style="left:532px;top:104px">Komandamız</span>
    <span class="foot-link" style="left:431px;top:129px">Biz kimik?</span>
    <span class="foot-link" style="left:532px;top:129px">Xidmətlərimiz</span>
    <span class="foot-link" style="left:431px;top:154px">T&amp;I Mərkəzi</span>
    <span class="foot-link" style="left:532px;top:154px">Təlimlər</span>
    <span class="foot-link" style="left:431px;top:179px">Əməkdaşlıq</span>
    <span class="foot-link" style="left:532px;top:179px">Əlaqə</span>
    <div class="abs foot-head" style="left:688px;top:69px">Contact</div>
    <div class="foot-link" style="left:688px;top:104px;display:flex;align-items:center;gap:5px">
      <svg width="9" height="9" viewBox="0 0 10 10"><path d="M2 0.5l2 2.3-1 1.3c.6 1.3 1.6 2.3 2.9 2.9l1.3-1 2.3 2-1 1.5C4.5 9.5.5 5.5.5 1.5z" fill="#fff"/></svg>+994 50 274 8812</div>
    <div class="foot-link" style="left:688px;top:129px;display:flex;align-items:center;gap:5px">
      <svg width="8" height="11" viewBox="0 0 8 11"><path d="M4 0a4 4 0 0 1 4 4c0 3-4 7-4 7S0 7 0 4a4 4 0 0 1 4-4z" fill="#fff"/><circle cx="4" cy="4" r="1.4" fill="#0e1128"/></svg>Çinar küçəsi 7B, Nizami rayonu</div>
    <div class="abs social" style="left:110px;top:232px"></div>
    <div class="abs social" style="left:155px;top:232px"></div>
    <div class="foot-link" style="left:676px;top:241px">Metrica Core 2021 © All right Reserved</div>
  </footer>

</div>
</body>
</html>
```